I'd like a business card that makes my company, Fenwright Marsh Associates Ltd stand out from the normal financial & IT services sector . It would be great to have a card that a potential client will think "wow" this is out of the norm , I'll give these guys a call. My business aims to provide consultancy services for financial and IT institutions but I'm looking to provide a newer approach that fits into today's social media rather than the standard "big 4" approach. My business helps companies assess their internal issues and aims to solve issues via business process re-engineering. The final design should have a balance of the maturity of the financial & IT sector with the fresh approach of the thriving social media sector

Target Market(s)

Business Managers and Directors, technical Managers and directors. Aged between 20 and 60 that handle project budgets

Industry/Entity Type

Financial

Requirements
Must have
• Must incorporate company logo currently being designed
Should not have
• No old-style fonts please.

```html
<!DOCTYPE html>
<html lang="en">
<head>
<meta charset="utf-8">
<title>Fenwright Marsh Associates Ltd — Business Card</title>
<link rel="stylesheet" href="https://fonts.googleapis.com/css2?family=Jost:wght@400;600&display=swap">
<style>
  :root {
    --backdrop: #e6e3df;
    --card-white: #ffffff;
    --brand-orange: #f26722;
    --brand-plum: #a11d5e;
    --ink: #3a3a3a;
    --text-light: #ffffff;
  }
  * { box-sizing: border-box; margin: 0; padding: 0; }
  html, body {
    width: 1200px; height: 1000px; overflow: hidden;
    background: var(--backdrop);
    font-family: "Jost", "Century Gothic", sans-serif;
  }
  .canvas { position: relative; width: 1200px; height: 1000px; }
  .card {
    position: absolute; left: 265px; width: 666px; height: 397px;
    box-shadow: 0 3px 8px rgba(0,0,0,0.25);
    overflow: hidden;
  }
  .card--front { top: 73px; background: var(--card-white); }
  .card--back { top: 532px; background: var(--brand-orange); }

  /* Front */
  .brand {
    position: absolute; left: 95px; top: 140px;
    display: flex; align-items: center; gap: 26px;
  }
  .brand__square { width: 125px; height: 115px; background: var(--brand-orange); }
  .brand__name {
    color: var(--ink); font-weight: 600; line-height: 1.15;
  }
  .brand__line1 { display: block; font-size: 28px; letter-spacing: 1px; text-transform: uppercase; }
  .brand__line2 { display: block; font-size: 19px; letter-spacing: 2px; text-align: center; margin-top: 4px; }

  /* Back */
  .back__band { position: absolute; left: 0; top: 0; width: 225px; height: 100%; background: var(--brand-plum); }
  .contact { position: absolute; left: 374px; top: 64px; color: var(--text-light); }
  .contact__name { font-size: 23px; font-weight: 600; letter-spacing: 0.5px; text-transform: uppercase; line-height: 1; }
  .contact__title { font-size: 17px; font-weight: 400; margin-top: 4px; }
  .contact__list { list-style: none; margin-top: 22px; }
  .contact__item {
    display: flex; align-items: flex-start; gap: 9px;
    font-size: 17px; line-height: 23px; margin-bottom: 6.5px;
  }
  .contact__item--web { margin-top: 4px; }
  .contact__item--address { margin-top: 4px; }
  .icon { width: 14px; height: 14px; margin-top: 4px; flex: none; fill: var(--text-light); }
</style>
</head>
<body>
<div class="canvas">
  <section class="card card--front">
    <div class="brand">
      <div class="brand__square"></div>
      <div class="brand__name">
        <span class="brand__line1">Fenwright Marsh</span>
        <span class="brand__line2">Associates Ltd</span>
      </div>
    </div>
  </section>

  <section class="card card--back">
    <div class="back__band"></div>
    <div class="contact">
      <h1 class="contact__name">Daniel Hollister</h1>
      <p class="contact__title">Executive Director</p>
      <ul class="contact__list">
        <li class="contact__item">
          <svg class="icon" viewBox="0 0 14 14"><path d="M4 0h6a1 1 0 0 1 1 1v12a1 1 0 0 1-1 1H4a1 1 0 0 1-1-1V1a1 1 0 0 1 1-1zm0.5 1.5v9.5h5V1.5z"/></svg>
          +61 400 218 563
        </li>
        <li class="contact__item">
          <svg class="icon" viewBox="0 0 14 14"><path d="M0 4c2-3 12-3 14 0v1.5h-3.5V4h-7v1.5H0zM3 7h8l2 6H1z"/></svg>
          +61 3 9112 4470
        </li>
        <li class="contact__item">
          <svg class="icon" viewBox="0 0 14 14"><path d="M3 0h8v4H3zM0 5h14v6h-3V8H3v3H0zM4 9h6v5H4z"/></svg>
          +61 3 9284 0619
        </li>
        <li class="contact__item">
          <svg class="icon" viewBox="0 0 14 14"><path d="M0 2h14v1L7 8 0 3zM0 4.5l7 5 7-5V12H0z"/></svg>
          info@fenwrightmarsh.co.uk
        </li>
        <li class="contact__item contact__item--web">
          <svg class="icon" viewBox="0 0 14 14"><circle cx="7" cy="7" r="6.2" fill="none" stroke="#fff" stroke-width="1.3"/><path d="M0.8 7h12.4M7 0.8v12.4" stroke="#fff" stroke-width="1.1"/><ellipse cx="7" cy="7" rx="2.8" ry="6.2" fill="none" stroke="#fff" stroke-width="1.1"/></svg>
          fenwrightmarsh.co.uk
        </li>
        <li class="contact__item contact__item--address">
          <svg class="icon" viewBox="0 0 14 14"><path d="M7 0a5 5 0 0 1 5 5c0 3.5-5 9-5 9S2 8.5 2 5a5 5 0 0 1 5-5zm0 3a2 2 0 1 0 0 4 2 2 0 0 0 0-4z"/></svg>
          <span>14 Carrow Lane<br>Eltham VIC 3095</span>
        </li>
      </ul>
    </div>
  </section>
</div>
</body>
</html>
```